Stanbrook Fire Services Pty Ltd

We need business cards for a company based in Perth, we install, service and maintain fire equipment.
On the front we want a great design with our logo and a small spot for our full company name, general company email address and office number. On the back we need space for our name, title, mobile number and email address on the back.

Target Market(s)

Facility managers and commercial/industrial building owners/occupiers.

Contact Information for Business Card

Font styles to use
Sans Serif

Requirements
Must have
• Please only submit 5 of your best samples.
Darker tones are preferred.
Nice to have
• We want to use, black, red and grey. Keep it modern and clean.
I've attached the company logo and a sample of a boarder we use on our emergency plans.
Should not have
• No preference. Let the designer choose.

```html
<!DOCTYPE html>
<html lang="en">
<head>
<meta charset="UTF-8">
<title>Stanbrook Fire Services – Business Cards</title>
<link href="https://fonts.googleapis.com/css2?family=Poppins:wght@400;500;600;700;800&display=swap" rel="stylesheet">
<style>
  :root {
    --backdrop: #2a2a2c;
    --fire-red: #f20d0d;
    --deep-red: #c40606;
    --ember: #e8501c;
    --smoke: #5a2a18;
    --ink: #1a1a1a;
    --steel-grey: #7a7a7a;
    --paper: #ffffff;
  }
  * { box-sizing: border-box; margin: 0; padding: 0; }
  html, body { width: 1200px; height: 880px; overflow: hidden; }
  body {
    background: var(--backdrop);
    font-family: "Poppins", sans-serif;
    position: relative;
  }
  .card {
    position: absolute;
    left: 270px;
    width: 660px;
    height: 377px;
    border-radius: 18px;
    overflow: hidden;
    box-shadow: 0 14px 30px rgba(0,0,0,0.45);
  }
  /* Front */
  .card--front { top: 40px; background: var(--fire-red); }
  .front__photo {
    position: absolute;
    top: 0; right: 0;
    width: 72%;
    height: 100%;
    background:
      radial-gradient(ellipse at 62% 40%, rgba(90,70,40,0.85) 0%, rgba(90,60,30,0.5) 35%, transparent 60%),
      radial-gradient(ellipse at 30% 70%, #ffb347 0%, #ff6a1a 30%, transparent 60%),
      linear-gradient(160deg, var(--smoke) 0%, #a8401a 45%, var(--ember) 75%, #f36a1d 100%);
    -webkit-mask-image: linear-gradient(to right, transparent 0%, #000 35%);
            mask-image: linear-gradient(to right, transparent 0%, #000 35%);
  }
  .front__wordmark {
    position: absolute;
    top: 86px; left: 52px;
    color: var(--paper);
    font-weight: 700;
    font-size: 52px;
    letter-spacing: 1px;
    line-height: 1;
  }
  .front__band {
    position: absolute;
    left: 0; right: 0;
    bottom: 34px;
    height: 62px;
    background: linear-gradient(to right, var(--fire-red) 0%, rgba(242,13,13,0.92) 100%);
    display: flex;
    align-items: center;
    padding-left: 52px;
  }
  .front__company {
    color: var(--paper);
    font-weight: 700;
    font-size: 27px;
    letter-spacing: 1.5px;
  }
  /* Back */
  .card--back { top: 463px; background: var(--paper); }
  .back__wordmark {
    position: absolute;
    top: 145px; left: 70px;
    color: var(--fire-red);
    font-weight: 700;
    font-size: 46px;
    letter-spacing: 1px;
    line-height: 1;
  }
  .back__divider {
    position: absolute;
    left: 365px; top: 95px;
    width: 1.5px; height: 150px;
    background: var(--ink);
  }
  .back__details {
    position: absolute;
    left: 390px; top: 92px;
    color: var(--ink);
    font-size: 13.5px;
    line-height: 1.35;
  }
  .back__name {
    color: var(--fire-red);
    font-weight: 700;
    font-size: 22px;
    line-height: 1.1;
  }
  .back__title { font-size: 15px; margin-bottom: 12px; }
  .back__address { margin-bottom: 6px; }
  .contact-line { display: flex; align-items: center; gap: 7px; }
  .contact-line svg { width: 15px; height: 15px; flex: none; }
  .back__stripes { position: absolute; left: 0; bottom: 0; width: 660px; height: 90px; }
</style>
</head>
<body>

<section class="card card--front">
  <div class="front__photo" role="img" aria-label="Photo of firefighters in protective gear and breathing apparatus spraying water into flames"></div>
  <div class="front__wordmark">STANBROOK</div>
  <div class="front__band">
    <span class="front__company">Stanbrook Fire Services Pty Ltd</span>
  </div>
</section>

<section class="card card--back">
  <div class="back__wordmark">STANBROOK</div>
  <div class="back__divider"></div>
  <div class="back__details">
    <div class="back__name">LIAM CARTER</div>
    <div class="back__title">Director</div>
    <div class="back__address">PO BOX 456 Harbour Road<br>Perth</div>
    <div class="contact-line">
      <svg viewBox="0 0 16 16" aria-hidden="true"><circle cx="8" cy="8" r="8" fill="#f20d0d"/><path d="M5.4 4.3l1.3 1.4-.7 1a5 5 0 0 0 2.3 2.3l1-.7 1.4 1.3-.8 1.2c-2.9-.3-5.3-2.7-5.6-5.6z" fill="#fff"/></svg>
      <span>0412 555 678</span>
    </div>
    <div class="contact-line">
      <svg viewBox="0 0 16 16" aria-hidden="true"><circle cx="8" cy="8" r="8" fill="#f20d0d"/><rect x="4" y="5.2" width="8" height="5.6" rx="0.6" fill="#fff"/><path d="M4.3 5.6L8 8.4l3.7-2.8" stroke="#f20d0d" stroke-width="0.9" fill="none"/></svg>
      <span>info@stanbrookfire.com</span>
    </div>
  </div>
  <svg class="back__stripes" viewBox="0 0 660 90" preserveAspectRatio="none" aria-hidden="true">
    <polygon points="0,90 0,80 40,70 80,90" fill="var(--fire-red)"/>
    <polygon points="60,90 110,56 170,44 120,90" fill="var(--steel-grey)"/>
    <polygon points="110,90 170,44 240,34 180,90" fill="var(--fire-red)"/>
    <polygon points="220,90 290,30 360,22 300,90" fill="var(--fire-red)"/>
    <polygon points="300,90 360,22 420,14 370,90" fill="var(--steel-grey)"/>
    <polygon points="370,90 420,14 490,8 440,90" fill="var(--fire-red)"/>
    <polygon points="470,90 520,6 580,2 540,90" fill="var(--steel-grey)"/>
    <polygon points="540,90 580,2 660,0 660,90" fill="var(--fire-red)"/>
  </svg>
</section>

</body>
</html>
```